Powerpoint design for spirits and cosmetics packaging company

We need a powerpoint template that will be used for company presentations, projects, award ceremonies etc... We are packaging in the wine and spirits sector as well as in the cosmetics sector. Our job is to package our customers' bottles in gift boxes, to carry out labeling, quality control, etc. We are based in Cognac.
We work for the big names in luxury: QDRT, Vellane Ostrow, Trelumo, Syvanne etc...
The template should be neat with at least 10 different slides.
Cover page, summary page, product description page (several), page including a schedule, price presentation page.

Target Market(s)

premium spirits and cosmetics

Industry/Entity Type

Spiritueux et cosmétique

Font styles to use
Sans Serif

Requirements
Must have
• My project must have the logo attached, the possibility to add / modify photos afterwards. Must have about ten different slides

```html
<!DOCTYPE html>
<html lang="en">
<head>
<meta charset="utf-8">
<title>Maison Verlac – Presentation Template</title>
<link href="https://fonts.googleapis.com/css2?family=Nunito:wght@700;800;900&family=Nunito+Sans:wght@400;600;700&display=swap" rel="stylesheet">
<style>
  :root{
    --page:#c9cacc;
    --red:#c8102e;
    --red-bright:#e8262a;
    --orange:#f7901e;
    --ink:#2b2b2b;
    --text:#3a3a3a;
    --row:#f0f0f3;
    --white:#ffffff;
  }
  *{box-sizing:border-box;margin:0;padding:0}
  html,body{width:1200px;height:3914px;overflow:hidden;background:var(--page)}
  body{position:relative;font-family:"Nunito Sans",Arial,sans-serif;color:var(--text)}
  .slide{position:absolute;left:102px;width:1001px;height:562px;background:var(--white);overflow:hidden}
  .photo{position:absolute}
  .brand{position:absolute;display:flex;align-items:flex-start;gap:8px}
  .brand-mark{width:30px;height:30px;background:var(--red);flex:none}
  .brand-name{font-family:"Nunito",sans-serif;font-weight:800;font-size:13px;line-height:13px;letter-spacing:1px;color:var(--red);text-transform:uppercase;padding-top:2px}
  .heading{position:absolute;font-family:"Nunito",sans-serif;font-weight:900;font-size:20px;color:var(--red);padding:6px 14px;letter-spacing:.3px}
  .heading::before,.heading::after{content:"";position:absolute;width:16px;height:16px}
  .heading::before{left:0;top:0;border-top:3px solid var(--red);border-left:3px solid var(--red)}
  .heading::after{right:0;bottom:0;border-bottom:3px solid var(--red);border-right:3px solid var(--red)}
  .body-text{font-size:11.3px;line-height:16.7px;text-align:justify}

  /* cover */
  .cover{top:94px}
  .cover .photo{inset:0;background:radial-gradient(circle at 45% 55%,#8a5a3a 0%,#5b4a3e 35%,#3d3a36 70%,#2d2e2c 100%)}
  .cover .brand{right:34px;top:20px}
  .cover-bar{position:absolute;left:0;top:392px;width:10px;height:110px;background:var(--red)}
  .cover-title{position:absolute;left:29px;top:385px;font-family:"Nunito",sans-serif;font-weight:900;font-size:38px;line-height:39px;color:var(--white);text-transform:uppercase}

  /* about */
  .about{top:728px}
  .about .brand{left:27px;top:20px}
  .about .heading{left:27px;top:123px}
  .about .body-text{position:absolute;left:27px;top:188px;width:292px}
  .about-frame{position:absolute;left:366px;top:21px;width:605px;height:520px;background:var(--orange)}
  .about-block{position:absolute;left:620px;top:0;width:381px;height:562px;background:var(--red-bright)}
  .about .photo{left:378px;top:33px;width:586px;height:495px;background:linear-gradient(160deg,#9aa6b3 0%,#6d7a88 45%,#d9dde2 75%,#8e969c 100%)}

  /* product */
  .product{top:1361px}
  .product .brand,.schedule .brand{left:27px;top:22px}
  .product .heading{left:207px;top:20px}
  .product-card{position:absolute;top:97px;width:459px}
  .product-card .photo{position:relative;width:459px;height:219px}
  .product-card h2{font-family:"Nunito",sans-serif;font-weight:900;font-size:18px;color:var(--red);margin-top:28px}
  .product-card .body-text{margin-top:10px}
  .spirits{left:26px}
  .spirits .photo{background:linear-gradient(135deg,#4a4a4c 0%,#8a5a2c 50%,#3a3a3c 100%)}
  .cosmetics{left:515px}
  .cosmetics .photo{background:linear-gradient(135deg,#6f6f70 0%,#a08468 55%,#5a5b5d 100%)}

  /* schedule */
  .schedule{top:1994px}
  .schedule .brand{left:33px}
  .schedule .heading{left:212px;top:20px}
  .milestone{position:absolute;top:117px;width:210px;height:400px;--accent:var(--red)}
  .milestone.alt{--accent:var(--orange)}
  .milestone .line{position:absolute;left:0;top:0;width:50px;height:383px;border-left:2px solid var(--accent);border-bottom:2px solid var(--accent)}
  .milestone .line::before{content:"";position:absolute;left:0;top:0;width:8px;border-top:2px solid var(--accent)}
  .milestone .line::after{content:"";position:absolute;right:-4px;bottom:-5px;width:8px;height:8px;border-radius:50%;background:var(--accent)}
  .milestone .year{position:absolute;left:18px;top:3px;font-family:"Nunito",sans-serif;font-weight:900;font-size:19px;color:var(--accent)}
  .milestone .tag{position:absolute;left:2px;top:35px;width:125px;height:26px;background:var(--accent);color:var(--white);font-family:"Nunito",sans-serif;font-weight:800;font-size:11px;line-height:26px;padding-left:20px}
  .milestone p{position:absolute;left:24px;top:85px;width:182px;font-size:10.6px;line-height:12.6px}

  /* pricing */
  .pricing{top:2628px}
  .pricing .brand{left:17px;top:20px}
  .pricing .heading{left:188px;top:20px}
  .plan-head{position:absolute;top:106px;left:20px;width:193px;height:49px;background:var(--ink);border-radius:24px 24px 0 0;color:var(--white);font-family:"Nunito",sans-serif;font-weight:800;font-size:15px;text-align:center;line-height:52px}
  .tier{position:absolute;width:135px;bottom:407px;border-radius:60px 60px 0 0;color:var(--white);font-family:"Nunito",sans-serif;font-weight:800;text-align:center;display:flex;flex-direction:column;justify-content:flex-end;padding-bottom:10px}
  .tier .price{font-size:23px;font-weight:900;line-height:26px}
  .tier .name{font-size:13px;line-height:16px}
  .tier.red{background:var(--red)}
  .tier.orange{background:var(--orange)}
  .plan-table{position:absolute;left:17px;top:155px;width:969px}
  .plan-row{position:relative;height:36.5px;font-size:11px;line-height:36.5px;padding-left:30px;color:var(--ink)}
  .plan-row:nth-child(odd){background:var(--row)}
  .plan-row.end{height:20px}
  .plan-row svg{position:absolute;top:9px;width:19px;height:19px}
  .c1{left:518px}.c2{left:649px}.c3{left:789px}.c4{left:924px}

  /* closing */
  .closing{top:3261px}
  .closing .photo{left:0;top:0;width:1001px;height:475px;background:linear-gradient(165deg,#8e9aa7 0%,#5f6b77 45%,#c9ced4 78%,#7f878c 100%)}
  .closing-title{position:absolute;left:0;right:0;top:197px;text-align:center}
  .closing-title span{display:inline-block;font-family:"Nunito",sans-serif;font-weight:900;font-size:58px;line-height:70px;color:var(--white);border-top:2px solid var(--white);border-bottom:2px solid var(--white);padding:0 4px}
  .footer{position:absolute;left:0;top:475px;width:1001px;height:87px}
  .footer .brand{left:17px;top:24px}
  .footer .brand-mark{width:40px;height:40px}
  .footer .brand-name{font-size:17px;line-height:18px}
  .footer-divider{position:absolute;left:246px;top:18px;width:2px;height:55px;background:var(--red)}
  .contact{position:absolute;top:32px;font-size:11.5px;line-height:18px;color:var(--ink)}
</style>
</head>
<body>
<svg width="0" height="0" style="position:absolute">
  <symbol id="tick" viewBox="0 0 20 20">
    <circle cx="10" cy="10" r="8.6" fill="none" stroke="#f7901e" stroke-width="1.6"/>
    <path d="M6 10.3l2.8 2.7L14 7.6" fill="none" stroke="#f7901e" stroke-width="1.8" stroke-linecap="round" stroke-linejoin="round"/>
  </symbol>
</svg>

<section class="slide cover">
  <div class="photo" role="img" aria-label="Hands inspecting a labelled cognac bottle on the packing line"></div>
  <div class="brand"><span class="brand-mark"></span><span class="brand-name">Maison<br>Verlac</span></div>
  <div class="cover-bar"></div>
  <h1 class="cover-title">Welcome to<br>Maison<br>Verlac</h1>
</section>

<section class="slide about">
  <div class="brand"><span class="brand-mark"></span><span class="brand-name">Maison<br>Verlac</span></div>
  <h2 class="heading">ABOUT US</h2>
  <p class="body-text">There are many variations of passages of Lorem Ipsum available, but the majority have suffered alteration in some form, by injected humour, or randomised words which don't look even slightly believable. If you are going to use a passage of Lorem Ipsum, you need to be sure there isn't anything embarrassing hidden in the middle of text. All the Lorem Ipsum generators on the Internet tend to repeat predefined chunks as necessary, making this the first true generator on the Internet. It uses a dictionary of over 200 Latin words, combined with a handful of model sentence structures, to generate Lorem Ipsum which looks reasonable. The generated Lorem Ipsum is therefore always free from repetition, injected humour, or non-characteristic words etc. The point of using Lorem Ipsum is that it has a more-or-less normal distribution of letters, as opposed to using 'Content here, content here', making it look like readable English. Many desktop publishing packages and web page editors now use</p>
  <div class="about-frame"></div>
  <div class="about-block"></div>
  <div class="photo" role="img" aria-label="Workers in masks filling bottles on a bottling line in the warehouse"></div>
</section>

<section class="slide product">
  <div class="brand"><span class="brand-mark"></span><span class="brand-name">Maison<br>Verlac</span></div>
  <h2 class="heading">PRODUCT</h2>
  <article class="product-card spirits">
    <div class="photo" role="img" aria-label="Gloved hands sealing the neck of an amber spirits bottle"></div>
    <h2>SPIRITS</h2>
    <p class="body-text">There are many variations of passages of Lorem Ipsum available, but the majority have suffered alteration in some form, by injected humour, or randomised words which don't look even slightly believable. If you are going to use a passage of Lorem Ipsum, you need to be sure there isn't anything embarrassing hidden in the middle of text. All the Lorem Ipsum generators on the Internet tend to repeat predefined chunks as necessary, making this the first true generator on the Internet. It uses a dictionary of over 200 Latin words, combined with a handful of model sentence structures, to generate Lorem Ipsum which looks reasonable. The generated Lorem Ipsum</p>
  </article>
  <article class="product-card cosmetics">
    <div class="photo" role="img" aria-label="Hand placing a cosmetic pump bottle into a gift box"></div>
    <h2>COSMETICS</h2>
    <p class="body-text">There are many variations of passages of Lorem Ipsum available, but the majority have suffered alteration in some form, by injected humour, or randomised words which don't look even slightly believable. If you are going to use a passage of Lorem Ipsum, you need to be sure there isn't anything embarrassing hidden in the middle of text. All the Lorem Ipsum generators on the Internet tend to repeat predefined chunks as necessary, making this the first true generator on the Internet. It uses a dictionary of over 200 Latin words, combined with a handful of model sentence structures, to generate Lorem Ipsum which looks reasonable. The generated Lorem Ipsum</p>
  </article>
</section>

<section class="slide schedule">
  <div class="brand"><span class="brand-mark"></span><span class="brand-name">Maison<br>Verlac</span></div>
  <h2 class="heading">SCHEDULE</h2>
  <div class="milestone" style="left:33px"><div class="line"></div><div class="year">2020</div><div class="tag">LOREM IPSUM</div>
    <p>There are many variations of passages of Lorem Ipsum available, but the majority have suffered alteration in some form, by injected humour, or randomised words which don't look even slightly believable. If you are going to use a passage of Lorem Ipsum, you need to be sure there isn't anything embarrassing hidden in the middle of text. All the Lorem Ipsum generators on the Internet tend to repeat predefined chunks as necessary, making this the first true generator on the Internet. It uses a dictionary of over 200 Latin words, combined with a handful of model sentence structures, to generat Lorem Ipsum which looks reasonable. The generated Lorem Ipsum is therefore always free from repetition, injected humour, or non-ch aracteristic wordse</p></div>
  <div class="milestone alt" style="left:277px"><div class="line"></div><div class="year">2021</div><div class="tag">LOREM IPSUM</div>
    <p>There are many variations of passages of Lorem Ipsum available, but the majority have suffered alteration in some form, by injected humour, or randomised words which don't look even slightly believable. If you are going to use a passage of Lorem Ipsum, you need to be sure there isn't anything embarrassing hidden in the middle of text. All the Lorem Ipsum generators on the Internet tend to repeat predefined chunks as necessary, making this the first true generator on the Internet. It uses a dictionary of over 200 Latin words, combined with a handful of model sentence structures, to generat Lorem Ipsum which looks reasonable. The generated Lorem Ipsum is therefore always free from repetition, injected humour, or non-ch aracteristic wordse</p></div>
  <div class="milestone" style="left:521px"><div class="line"></div><div class="year">2022</div><div class="tag">LOREM IPSUM</div>
    <p>There are many variations of passages of Lorem Ipsum available, but the majority have suffered alteration in some form, by injected humour, or randomised words which don't look even slightly believable. If you are going to use a passage of Lorem Ipsum, you need to be sure there isn't anything embarrassing hidden in the middle of text. All the Lorem Ipsum generators on the Internet tend to repeat predefined chunks as necessary, making this the first true generator on the Internet. It uses a dictionary of over 200 Latin words, combined with a handful of model sentence structures, to generat Lorem Ipsum which looks reasonable. The generated Lorem Ipsum is therefore always free from repetition, injected humour, or non-ch aracteristic wordse</p></div>
  <div class="milestone alt" style="left:758px"><div class="line"></div><div class="year">2023</div><div class="tag">LOREM IPSUM</div>
    <p>There are many variations of passages of Lorem Ipsum available, but the majority have suffered alteration in some form, by injected humour, or randomised words which don't look even slightly believable. If you are going to use a passage of Lorem Ipsum, you need to be sure there isn't anything embarrassing hidden in the middle of text. All the Lorem Ipsum generators on the Internet tend to repeat predefined chunks as necessary, making this the first true generator on the Internet. It uses a dictionary of over 200 Latin words, combined with a handful of model sentence structures, to generat Lorem Ipsum which looks reasonable. The generated Lorem Ipsum is therefore always free from repetition, injected humour, or non-ch aracteristic wordse</p></div>
</section>

<section class="slide pricing">
  <div class="brand"><span class="brand-mark"></span><span class="brand-name">Maison<br>Verlac</span></div>
  <h2 class="heading">PRICING</h2>
  <div class="plan-head">LOREM IPSUM</div>
  <div class="tier red" style="left:445px;height:71px"><span class="name">FREE</span></div>
  <div class="tier orange" style="left:580px;height:84px"><span class="price">$12</span><span class="name">STARTUP</span></div>
  <div class="tier red" style="left:715px;height:93px"><span class="price">$50</span><span class="name">PRO</span></div>
  <div class="tier orange" style="left:850px;height:107px"><span class="price">$150</span><span class="name">VIP</span></div>
  <div class="plan-table">
    <div class="plan-row">Lorem ipsum dolor sit amet, consectetur<svg class="c1"><use href="#tick"/></svg><svg class="c2"><use href="#tick"/></svg><svg class="c3"><use href="#tick"/></svg><svg class="c4"><use href="#tick"/></svg></div>
    <div class="plan-row">In vestibulum erat ac ipsum faucibus<svg class="c1"><use href="#tick"/></svg><svg class="c2"><use href="#tick"/></svg><svg class="c3"><use href="#tick"/></svg><svg class="c4"><use href="#tick"/></svg></div>
    <div class="plan-row">Praesent lobortis arcu et efficitur ultrices.<svg class="c1"><use href="#tick"/></svg><svg class="c2"><use href="#tick"/></svg><svg class="c3"><use href="#tick"/></svg><svg class="c4"><use href="#tick"/></svg></div>
    <div class="plan-row">Quisque quis dolor consectetur.<svg class="c1"><use href="#tick"/></svg><svg class="c2"><use href="#tick"/></svg><svg class="c3"><use href="#tick"/></svg><svg class="c4"><use href="#tick"/></svg></div>
    <div class="plan-row">Nunc in leo sit amet dui tincidunt<svg class="c1"><use href="#tick"/></svg><svg class="c2"><use href="#tick"/></svg><svg class="c3"><use href="#tick"/></svg><svg class="c4"><use href="#tick"/></svg></div>
    <div class="plan-row">Integer ut mi ut nibh sempe<svg class="c1"><use href="#tick"/></svg><svg class="c2"><use href="#tick"/></svg><svg class="c3"><use href="#tick"/></svg><svg class="c4"><use href="#tick"/></svg></div>
    <div class="plan-row">Quisque elementum ex eget pla<svg class="c1"><use href="#tick"/></svg><svg class="c2"><use href="#tick"/></svg><svg class="c3"><use href="#tick"/></svg><svg class="c4"><use href="#tick"/></svg></div>
    <div class="plan-row">Etiam nec tortor sollicitudin, imperdiet<svg class="c2"><use href="#tick"/></svg><svg class="c3"><use href="#tick"/></svg><svg class="c4"><use href="#tick"/></svg></div>
    <div class="plan-row">Fusce facilisis erat a neque conse<svg class="c2"><use href="#tick"/></svg><svg class="c3"><use href="#tick"/></svg><svg class="c4"><use href="#tick"/></svg></div>
    <div class="plan-row">Nullam quis dui ac tellus<svg class="c3"><use href="#tick"/></svg><svg class="c4"><use href="#tick"/></svg></div>
    <div class="plan-row end"></div>
  </div>
</section>

<section class="slide closing">
  <div class="photo" role="img" aria-label="Packing team working along the bottling line in the warehouse"></div>
  <div class="closing-title"><span>THANK YOU</span></div>
  <footer class="footer">
    <div class="brand"><span class="brand-mark"></span><span class="brand-name">Maison<br>Verlac</span></div>
    <div class="footer-divider"></div>
    <div class="contact" style="left:283px">218 Orchard Lane<br>Fairhaven, MA 02719</div>
    <div class="contact" style="left:452px">Call us<br>+1 888 888 8888</div>
    <div class="contact" style="left:588px">Email us<br>info@maisonverlac.com</div>
  </footer>
</section>
</body>
</html>
```